Business Card for Vorlo Parts Wholesale supplier

Hi There! I need a new business card for our company. We are specialized in selling Vorlo parts, mostly we sell new LCD screens for uDialr and oTabs. I would like to see that back in the design.

You can find the colors and logo's on our website: www.darvok.nl

Industry/Entity Type

Business

Contact Information for Business Card

My Details:
Bas Hollink

Phone: 0031627381946
E-mail: Bas@darvok.nl

Slogan: "Because Quality Matters"

Font styles to use
Sans Serif

Colors

Designer to choose colors to be used in the design.

Requirements
Must have
• A Black backside with the Darvok logo on it. The front side should be clean with only my contact details.
• But I'm also open for something really different or awesome!
Nice to have
• Remember that we are in the parts & repairing industry, So i'll be handing those business cards mainly to repair companies. Maybe you can do something with that thought :)

```html
<!DOCTYPE html>
<html lang="en">
<head>
<meta charset="utf-8">
<title>Darvok Business Card</title>
<link href="https://fonts.googleapis.com/css2?family=Roboto:wght@400;500;700&display=swap" rel="stylesheet">
<style>
  :root {
    --bg: #4a423d;
    --card: #161616;
    --card-back: #121212;
    --gloss: #2c2c2c;
    --orange: #f26b1d;
    --white: #f2f2f2;
    --muted: #d6d6d6;
  }
  * { box-sizing: border-box; margin: 0; padding: 0; }
  html, body {
    width: 1200px; height: 715px; overflow: hidden;
    background: var(--bg);
    font-family: "Roboto", Arial, sans-serif;
  }
  .canvas {
    position: relative; width: 1200px; height: 715px;
  }
  .card {
    position: absolute; top: 207px;
    width: 525px; height: 300px;
    border-radius: 4px;
    box-shadow: 0 14px 30px rgba(0,0,0,0.45);
  }
  .card--back {
    left: 50px; background: var(--card-back);
    display: flex; align-items: center; justify-content: center;
  }
  .back-mark {
    display: flex; align-items: center; gap: 14px;
  }
  .back-mark__square {
    width: 44px; height: 44px; background: var(--gloss);
  }
  .back-mark__name {
    font-size: 48px; font-weight: 700; color: var(--gloss); letter-spacing: 1px;
  }
  .card--front {
    left: 625px; background: var(--card);
  }
  .brand {
    position: absolute; left: 40px; top: 110px;
  }
  .brand__row {
    display: flex; align-items: center; gap: 10px;
  }
  .brand__square {
    width: 40px; height: 40px; background: var(--orange);
  }
  .brand__name {
    font-size: 44px; font-weight: 700; color: var(--white); line-height: 1;
  }
  .brand__slogan {
    margin-top: 6px; margin-left: 50px;
    font-size: 15px; color: var(--white);
  }
  .contact {
    position: absolute; left: 320px; top: 150px;
  }
  .contact__name {
    font-size: 19px; font-weight: 700; color: var(--orange);
  }
  .contact__role {
    font-size: 12px; color: var(--muted); margin-top: 2px; margin-bottom: 14px;
  }
  .contact__list { list-style: none; }
  .contact__item {
    display: flex; align-items: center; gap: 10px;
    font-size: 14px; color: var(--white); margin-bottom: 6px;
  }
  .contact__icon { width: 13px; height: 13px; flex: none; }
</style>
</head>
<body>
<main class="canvas">
  <section class="card card--back" aria-label="Card back">
    <div class="back-mark">
      <span class="back-mark__square"></span>
      <span class="back-mark__name">darvok</span>
    </div>
  </section>

  <section class="card card--front" aria-label="Card front">
    <div class="brand">
      <div class="brand__row">
        <span class="brand__square"></span>
        <span class="brand__name">darvok</span>
      </div>
      <p class="brand__slogan">Because Quality Matters</p>
    </div>

    <div class="contact">
      <p class="contact__name">Bas Hollink</p>
      <p class="contact__role">Managing Director</p>
      <ul class="contact__list">
        <li class="contact__item">
          <svg class="contact__icon" viewBox="0 0 16 16" aria-hidden="true"><path fill="#f26b1d" d="M3.6 1.2l2.3 2.6-1.3 1.9c.9 2 2.4 3.6 4.5 4.6l1.9-1.3 2.6 2.3-1.4 2.6C6.9 13.6 2.4 9.2 1.1 2.6z"/></svg>
          0031627381946
        </li>
        <li class="contact__item">
          <svg class="contact__icon" viewBox="0 0 16 16" aria-hidden="true"><rect x="1" y="3" width="14" height="10" fill="#f26b1d"/><path d="M1 3l7 5.5L15 3" fill="none" stroke="#161616" stroke-width="1.4"/></svg>
          Bas@darvok.nl
        </li>
        <li class="contact__item">
          <svg class="contact__icon" viewBox="0 0 16 16" aria-hidden="true"><circle cx="8" cy="8" r="7" fill="#f26b1d"/><path d="M1 8h14M8 1c-3 3.5-3 10.5 0 14M8 1c3 3.5 3 10.5 0 14" fill="none" stroke="#161616" stroke-width="1.1"/></svg>
          www.darvok.nl
        </li>
      </ul>
    </div>
  </section>
</main>
</body>
</html>
```